Simplified Double Diamond Diagram for Book

I need a simplified version of the Double Diamond Diagram for a book I am working on. I would like to represent the diagram with the following image/text:
- Two diamonds connected (as in each of the sample photos)
- Inclusion of "Diverge" "Converge" above each of the sides of the diamonds as shown in sample image 1 - without elaborative text
- Inclusion of "Problem" and "Solution" in each diamond as is shown in the example image 2
- I need a color version and black/white version of the image that can be turned into a mono-color version in the book.

```html
<!DOCTYPE html>
<html lang="en">
<head>
<meta charset="utf-8">
<title>Double Diamond Diagram</title>
<link rel="stylesheet" href="https://fonts.googleapis.com/css2?family=Montserrat:wght@900&display=swap">
<style>
  :root {
    --paper: #ffffff;
    --ink: #231f20;
    --label-grey: #58595b;
    --phase-grey: #d1d3d4;
    --guide-grey: #c8c8c8;
    --title-grey: #bcbcbc;
    --blue-light: #a6cee3;
    --blue: #1f78b4;
    --blue-deep: #0d5a8c;
    --green-light: #b2df8a;
    --green: #33a02c;
    --green-deep: #107510;
    --phase-white: #ffffff;
  }
  html, body {
    margin: 0;
    padding: 0;
    width: 1084px;
    height: 1200px;
    overflow: hidden;
    background: var(--paper);
  }
  .diagram-sheet {
    display: block;
    width: 1084px;
    height: 1200px;
    font-family: "Montserrat", "Arial Black", sans-serif;
    font-weight: 900;
  }
  .diagram-sheet text {
    text-anchor: middle;
    dominant-baseline: central;
  }
  .mono-outline { fill: none; stroke: var(--ink); stroke-width: 3.5; stroke-linejoin: miter; }
  .mono-guide { stroke: var(--guide-grey); stroke-width: 2.5; stroke-dasharray: 4 4; }
  .mono-step { fill: var(--label-grey); font-size: 25px; }
  .mono-phase { fill: var(--phase-grey); font-size: 30px; }
  .diagram-title { fill: var(--title-grey); font-size: 32px; letter-spacing: 0.5px; }

  .blue-diverge-fill { fill: var(--blue-light); }
  .blue-converge-fill { fill: var(--blue); }
  .blue-edge { fill: none; stroke: var(--blue); stroke-width: 5; }
  .blue-edge-deep { fill: none; stroke: var(--blue-deep); stroke-width: 5; }
  .blue-step { fill: var(--blue); font-size: 25px; }

  .green-diverge-fill { fill: var(--green-light); }
  .green-converge-fill { fill: var(--green); }
  .green-edge { fill: none; stroke: var(--green); stroke-width: 5; }
  .green-edge-deep { fill: none; stroke: var(--green-deep); stroke-width: 5; }
  .green-step { fill: var(--green); font-size: 25px; }

  .colour-phase { fill: var(--phase-white); font-size: 30px; }
</style>
</head>
<body>
<svg class="diagram-sheet" viewBox="0 0 1084 1200" xmlns="http://www.w3.org/2000/svg" role="img" aria-label="Double diamond diagram in mono and colour versions">

  <!-- Mono version -->
  <g class="mono-version">
    <line class="mono-guide" x1="335" y1="128" x2="335" y2="524"/>
    <line class="mono-guide" x1="741" y1="128" x2="741" y2="524"/>
    <polygon class="mono-outline" points="335,124 537,326 335,527 134,326"/>
    <polygon class="mono-outline" points="741,124 943,326 741,527 539,326"/>
    <text class="mono-phase" x="335" y="327">PROBLEM</text>
    <text class="mono-phase" x="741" y="325">SOLUTION</text>
    <text class="mono-step" transform="translate(210 210) rotate(-45)">DIVERGE</text>
    <text class="mono-step" transform="translate(459 213) rotate(45)">CONVERGE</text>
    <text class="mono-step" transform="translate(619 210) rotate(-45)">DIVERGE</text>
    <text class="mono-step" transform="translate(870 213) rotate(45)">CONVERGE</text>
  </g>

  <text class="diagram-title" x="542" y="620">DIAMOND DIAGRAM</text>

  <!-- Colour version -->
  <g class="colour-version">
    <g class="problem-diamond">
      <polygon class="blue-diverge-fill" points="328,699 328,1114 123,906"/>
      <polygon class="blue-converge-fill" points="328,699 534,906 328,1114"/>
      <polyline class="blue-edge" points="97,880 123,906 97,933"/>
      <polyline class="blue-edge" points="328,1114 123,906 328,699"/>
      <polyline class="blue-edge-deep" points="328,699 534,906 328,1114"/>
      <text class="colour-phase" x="328" y="908">PROBLEM</text>
      <text class="blue-step" transform="translate(203 791) rotate(-45)">DIVERGE</text>
      <text class="blue-step" transform="translate(451 794) rotate(45)">CONVERGE</text>
    </g>
    <g class="solution-diamond">
      <polygon class="green-diverge-fill" points="741,699 741,1114 536,906"/>
      <polygon class="green-converge-fill" points="741,699 946,906 741,1114"/>
      <polyline class="green-edge" points="741,1114 536,906 741,699"/>
      <polyline class="green-edge-deep" points="741,699 946,906 741,1114"/>
      <polyline class="green-edge-deep" points="972,880 946,906 972,933"/>
      <text class="colour-phase" x="742" y="907">SOLUTION</text>
      <text class="green-step" transform="translate(617 789) rotate(-45)">DIVERGE</text>
      <text class="green-step" transform="translate(870 794) rotate(45)">CONVERGE</text>
    </g>
  </g>
</svg>
</body>
</html>
```